A Cool Business Card so My Son can Network with People, Especially People in the Entertainment Business. Something that stands out and;Pops:*) He's an Entertainer goes by the ☆Kelso Dune KD Please include His Social Media that you will see and Contact Numbers as well in the pics. Submitted Please Hook It Up. Thanks!

Contact Information for Business Card:

A Cool Hip-hop ,Entertainer Design for My 16 Year old Son. He Sings,Raps,Actor,Dancer and Radio Personality as well. Something that stands out from the rest of the Business Cards & Pops. He's A Star Already it's only a matter of Time Until He Becomes A Superstar.

Thank You For Your Help!

Target Market(s)

18-40 y/o

Industry/Entity Type

Entertainment Industry

Contact Information for Business Card

To promote my artistry to the public
Im a Singer,Rapper,Dancer,Actor&Model

Font styles to use
Serif

Requirements
Must have
• artist name- Kelso Dune KD
• social media connections
• which are on the pics. downloaded.
Nice to have
• *Kelso Dune* KD
• Social Media Info as well as cell phone info located in downloads:*}
• Make it pop,add some of the Pics. Be Creative He is a Future Superstar:*)
Should not have
• Make it Amazing But also readable for His important info But make the Card off the chain any colors dont make it Girly He is a 16 year old Teenager. I left enough downloads of Pics. that someone who is Creative can make something Wonderful. Then whoever that is will work with Us on other Projects Including makin a CD Cover:.)

```html
<!DOCTYPE html>
<html lang="en">
<head>
<meta charset="utf-8">
<title>Kelso Dune KD — Business Card</title>
<link href="https://fonts.googleapis.com/css2?family=Delius&family=Kalam:wght@400&display=swap" rel="stylesheet">
<style>
  :root{
    --stage:#1f1d1d;
    --paper:#ffffff;
    --ink:#111111;
    --band-dark:#1a1a1a;
    --band-mid:#3a3a3a;
    --grunge:#2a2a2a;
    --icon-tile:#d6d6d6;
  }
  *{box-sizing:border-box;margin:0;padding:0}
  html,body{width:1200px;height:1200px;overflow:hidden;background:var(--stage)}
  .stage{position:relative;width:1200px;height:1200px}
  .card{position:absolute;left:120px;width:960px;height:549px;background:var(--paper);overflow:hidden}
  .card--front{top:34px}
  .card--back{top:617px}

  /* front */
  .grunge-frame{position:absolute;inset:0;
    background:radial-gradient(ellipse 62% 58% at 50% 50%, var(--paper) 70%, #bdbdbd 86%, var(--grunge) 100%)}
  .front-illustration{position:absolute;left:420px;top:96px;width:120px;height:140px;
    background:linear-gradient(180deg,#4a4a4a,#0d0d0d);border-radius:4px}
  .artist-name{position:absolute;left:0;right:0;top:236px;text-align:center;
    font-family:"Delius",cursive;font-size:112px;line-height:1;color:var(--ink)}
  .front-roles{position:absolute;left:0;right:0;top:382px;text-align:center;
    font-family:"Delius",cursive;font-size:28px;color:var(--ink);letter-spacing:.5px}

  /* back */
  .dark-band{position:absolute;left:0;right:0;top:120px;height:320px;
    background:linear-gradient(100deg,var(--band-dark) 0%,var(--band-mid) 45%,var(--band-dark) 100%)}
  .socials{position:absolute;left:40px;top:148px;width:440px;list-style:none}
  .socials li{display:flex;align-items:center;height:64px;gap:16px;white-space:nowrap;
    font-family:"Kalam",cursive;font-size:26px;color:var(--paper)}
  .socials .tile{width:32px;height:32px;background:var(--icon-tile);border-radius:4px;flex:none}
  .back-illustration{position:absolute;left:500px;top:22px;width:150px;height:230px;
    background:linear-gradient(180deg,#555,#0d0d0d);border-radius:4px}
  .monogram{position:absolute;left:500px;top:262px;width:150px;height:164px;background:var(--paper);
    display:flex;align-items:center;justify-content:center;
    font-family:"Delius",cursive;font-size:84px;color:var(--ink)}
  .contacts{position:absolute;right:48px;top:170px;width:220px;list-style:none;text-align:right}
  .contacts li{font-family:"Kalam",cursive;font-size:28px;color:var(--paper);margin-bottom:22px;white-space:nowrap}
  .contacts svg{display:block;margin:0 0 6px auto}
  .back-roles{position:absolute;left:0;right:0;top:462px;text-align:center;
    font-family:"Delius",cursive;font-size:36px;color:var(--ink)}
</style>
</head>
<body>
<main class="stage">
  <section class="card card--front">
    <div class="grunge-frame" role="img" aria-label="Distressed black grunge texture around the card edges"></div>
    <div class="front-illustration" role="img" aria-label="Black and white illustration of the artist pointing forward"></div>
    <h1 class="artist-name">Kelso Dune</h1>
    <p class="front-roles">Singer ★ Rapper ★ Dancer ★ Actor ★ Model</p>
  </section>

  <section class="card card--back">
    <div class="dark-band" role="img" aria-label="Dark grunge textured band"></div>
    <ul class="socials">
      <li><span class="tile"></span>KelsoduneKD</li>
      <li><span class="tile"></span>KelsoduneKD</li>
      <li><span class="tile"></span>@therealkelsodunekd</li>
      <li><span class="tile"></span>kelsodune@example.com</li>
    </ul>
    <div class="back-illustration" role="img" aria-label="Black and white illustration of the artist pointing forward"></div>
    <div class="monogram">KD</div>
    <ul class="contacts">
      <li>
        <svg width="30" height="30" viewBox="0 0 30 30" aria-hidden="true"><rect width="30" height="30" rx="4" fill="#fff"/><path d="M10 7l3 3-2 3c1 2 3 4 5 5l3-2 3 3-2 3c-6 0-13-7-13-13z" fill="#111"/></svg>
        555-014-2837
      </li>
      <li>
        <svg width="30" height="30" viewBox="0 0 30 30" aria-hidden="true"><rect width="30" height="30" rx="4" fill="#fff"/><rect x="10" y="5" width="10" height="20" rx="2" fill="none" stroke="#111" stroke-width="2"/><circle cx="15" cy="22" r="1.2" fill="#111"/></svg>
        555-019-6420
      </li>
    </ul>
    <p class="back-roles">Singer ★ Rapper ★ Dancer ★ Actor ★ Model</p>
  </section>
</main>
</body>
</html>
```